BRANDHILL real estate family office

Hello, Our business is a real estate intermediation activity on high-end goods (amounts exceeding € 10m) for corporate and private clients. You can see our logo on the site www.brandhill-demo.fr We would like to keep that spirit with the hexagon that represents France (transactions between Monaco and Saint Tropez, Courchevel and Paris). And the "baseline" that is "real estate family office". The corporate logo should be and can be printed by embossing (relief). We must integrate the name, first name, phone, email and website. Finally, to imbibe the spirit of business, here is a detail of the activity. "Genuine consulting firm in real estate investments, BRANDHILL works with its customers as a specialized player in the high-end markets, we are recognized for our ultra-confidential approach and tailor-made, as well as the quality of our network. We broadcast any information on the market and we work exclusively through a strong relationship we have developed over the years. BRANDHILL is active on the French Riviera (from Monaco to Saint-Tropez), the Alps (Courchevel, Méribel, Megève) and Paris (essentially market premium). Always looking for opportunities for our clients, we work on two investment areas: residential luxury real estate (properties, vineyards, mansions, land, etc.) commercial real estate (empty office buildings or yield, hotel properties, land, etc.) "

Target Market(s)

High foreign end customers. corporate and private.

Industry/Entity Type

Real Estate

Contact Information for Business Card

LOGO
baseline
Laurent Dufossé
+33(0)6.41.57.09.64
ld@brandhill-demo.fr
www.brandhill-demo.fr

Font styles to use
Serif

Colors
cedeed
0255a3
3277b5
85abd2
85cae6
34a7d7
0792cd
cfdeed
1b1b1b

Requirements
Must have
• see description

```html
<!DOCTYPE html>
<html lang="fr">
<head>
<meta charset="utf-8">
<title>BRANDHILL – cartes de visite</title>
<link rel="stylesheet" href="https://fonts.googleapis.com/css2?family=Arimo:wght@400;700&family=Montserrat:wght@300&display=swap">
<style>
  :root {
    --backdrop: #e3e3e3;
    --card-white: #f5f5f6;
    --brand-blue: #233f98;
    --brand-blue-light: #2d4ba6;
    --name-blue: #2a3f9e;
    --mark-grey: #9b9b9d;
    --ink: #1b1b1b;
    --paper-white: #ffffff;
  }
  * { margin: 0; padding: 0; box-sizing: border-box; }
  html, body {
    width: 1200px; height: 750px; overflow: hidden;
    background: var(--backdrop);
  }
  .canvas {
    width: 1200px; height: 750px;
    display: flex; align-items: center; justify-content: center; gap: 50px;
  }
  .card {
    position: relative;
    width: 525px; height: 300px;
    border-radius: 26px;
    overflow: hidden;
    box-shadow: 0 6px 18px rgba(0,0,0,0.12);
  }

  /* Front: identity side */
  .card--front { background: var(--card-white); }
  .front-brand {
    position: absolute; left: 38px; top: 50%;
    transform: translateY(-50%);
    width: 180px;
    display: flex; align-items: center; gap: 10px;
    font-family: "Arimo", Arial, sans-serif;
    font-weight: 700; font-size: 22px; letter-spacing: 2px;
    color: var(--mark-grey);
  }
  .front-brand__square {
    width: 14px; height: 14px; background: var(--mark-grey); flex: none;
  }
  .contact {
    position: absolute; right: 34px; top: 78px;
    width: 250px; text-align: right;
    font-family: "Arimo", Arial, sans-serif;
  }
  .contact__name {
    font-weight: 700; font-size: 17px; color: var(--name-blue);
    padding-bottom: 6px;
    border-bottom: 1.5px solid var(--ink);
  }
  .contact__line {
    font-size: 13px; color: var(--ink); margin-top: 7px;
  }

  /* Back: brand side */
  .card--back {
    background: linear-gradient(135deg, var(--brand-blue-light), var(--brand-blue));
  }
  .rule {
    position: absolute; height: 4px; background: var(--paper-white); opacity: 0.9;
  }
  .rule--top { right: 0; top: 112px; width: 105px; }
  .rule--bottom { left: 0; top: 262px; width: 115px; }
  .logo-lockup {
    position: absolute; left: 140px; top: 118px;
    color: var(--paper-white);
  }
  .logo-lockup__name {
    font-family: "Arimo", Arial, sans-serif;
    font-weight: 400; font-size: 30px; letter-spacing: 5px; line-height: 1;
  }
  .logo-lockup__baseline {
    font-family: "Montserrat", Arial, sans-serif;
    font-weight: 300; font-size: 10px; letter-spacing: 1.4px;
    margin-top: 3px; text-align: right;
  }
  .website {
    position: absolute; left: 0; right: 0; top: 198px;
    text-align: center;
    font-family: "Arimo", Arial, sans-serif;
    font-weight: 700; font-size: 13px; color: var(--paper-white);
  }
</style>
</head>
<body>
  <main class="canvas">
    <section class="card card--front" aria-label="Recto">
      <div class="front-brand"><span class="front-brand__square"></span>BRANDHILL</div>
      <div class="contact">
        <p class="contact__name">Laurent Dufossé</p>
        <p class="contact__line">+33(0)6.41.57.09.64</p>
        <p class="contact__line">ld@brandhill-demo.fr</p>
      </div>
    </section>

    <section class="card card--back" aria-label="Verso">
      <span class="rule rule--top"></span>
      <div class="logo-lockup">
        <p class="logo-lockup__name">BRANDHILL</p>
        <p class="logo-lockup__baseline">real estate family office</p>
      </div>
      <p class="website">www.brandhill-demo.fr</p>
      <span class="rule rule--bottom"></span>
    </section>
  </main>
</body>
</html>
```